Halvorsen Business Card/Stationary
Halvorsen
Project: Halvorsen Business Card/Stationary
Halvorsen Business Card/Stationary -
Creative Brief
Professional
R. Gordon Halvorsen
President
3847 Marlow Bend P.O. Box 6194 Lakemont, Norland 44915
ghalvorsen@halvorsenllc.example
www.halvorsenllc.example

```html
<!DOCTYPE html>
<html lang="en">
<head>
<meta charset="utf-8">
<title>Halvorsen Business Card</title>
<link href="https://fonts.googleapis.com/css2?family=Arimo:wght@400;700&display=swap" rel="stylesheet">
<style>
  :root {
    --page: #ffffff;
    --card: #050505;
    --rim: #9a9a9a;
    --rim-dark: #3a3a3a;
    --silver: #c9c9c9;
    --text: #e6e6e6;
    --mark: #8c8c8c;
  }
  * { margin: 0; padding: 0; box-sizing: border-box; }
  html, body {
    width: 1200px; height: 758px; overflow: hidden;
    background: var(--page);
    font-family: "Arimo", Arial, sans-serif;
  }
  .canvas { position: relative; width: 1200px; height: 758px; }
  .card {
    position: absolute;
    background: linear-gradient(160deg, #1a1a1a 0%, var(--card) 35%, var(--card) 100%);
    border: 5px solid var(--rim);
    box-shadow: 0 0 0 2px var(--rim-dark), 3px 4px 8px rgba(0,0,0,.35);
    color: var(--text);
  }
  .card--portrait { left: 65px; top: 115px; width: 386px; height: 600px; border-radius: 34px 10px 34px 10px; }
  .card--landscape { left: 482px; top: 192px; width: 651px; height: 374px; border-radius: 34px 10px 34px 10px; }
  .card > * { position: absolute; line-height: 1; white-space: nowrap; }

  .brand-dot { width: 110px; height: 110px; border-radius: 50%; background: var(--mark); }
  .wordmark { font-weight: 700; font-size: 40px; letter-spacing: 2px; color: var(--silver); }
  .name { font-weight: 700; font-size: 27px; color: var(--text); }
  .title { font-size: 18px; color: var(--text); }
  .line { font-size: 16px; color: var(--text); }
  .line .label { display: inline-block; margin-right: 10px; }

  /* portrait */
  .card--portrait .center { left: 0; width: 376px; text-align: center; }
  .card--portrait .brand-dot { left: 133px; top: 40px; }

  /* landscape */
  .card--landscape .brand-dot { left: 108px; top: 40px; }
  .card--landscape .wordmark { left: 30px; width: 336px; text-align: center; }
  .card--landscape .right { right: 36px; text-align: right; }
</style>
</head>
<body>
<main class="canvas">

  <section class="card card--portrait" aria-label="Vertical business card">
    <div class="brand-dot"></div>
    <div class="wordmark center" style="top:166px">HALVORSEN</div>
    <div class="name center" style="top:246px">R. Gordon Halvorsen</div>
    <div class="title center" style="top:281px">President</div>
    <div class="line center" style="top:330px">3847 Marlow Bend</div>
    <div class="line center" style="top:357px">P.O. Box 6194</div>
    <div class="line center" style="top:383px">Lakemont, Norland 44915</div>
    <div class="line center" style="top:438px"><span class="label">Phone</span>1 555 010 0148</div>
    <div class="line center" style="top:465px"><span class="label">Cell</span>1 555 010 0193</div>
    <div class="line center" style="top:491px"><span class="label">Fax</span>1 555 010 0177</div>
    <div class="line center" style="top:539px">ghalvorsen@halvorsenllc.example</div>
    <div class="line center" style="top:565px">www.halvorsenllc.example</div>
  </section>

  <section class="card card--landscape" aria-label="Horizontal business card">
    <div class="brand-dot"></div>
    <div class="wordmark" style="top:214px">HALVORSEN</div>
    <div class="name" style="left:50px; top:282px">R. Gordon Halvorsen</div>
    <div class="title" style="left:50px; top:313px">President</div>
    <div class="line right" style="top:45px">3847 Marlow Bend</div>
    <div class="line right" style="top:71px">P.O. Box 6194</div>
    <div class="line right" style="top:98px">Lakemont, Norland 44915</div>
    <div class="line right" style="top:153px"><span class="label">Phone</span>1 555 010 0148</div>
    <div class="line right" style="top:179px"><span class="label">Cell</span>1 555 010 0193</div>
    <div class="line right" style="top:206px"><span class="label">Fax</span>1 555 010 0177</div>
    <div class="line right" style="top:285px">ghalvorsen@halvorsenllc.example</div>
    <div class="line right" style="top:311px">www.halvorsenllc.example</div>
  </section>

</main>
</body>
</html>
```